Heat and air plumbing company needing eye catching van wrap

Looking for van wrap for 2012 Torvane x340. Would like the layout to be like the red blue and white just like the pic I’m sending. Would like the logo to be like the blue van with the ice cubes. So basically I want the red white blue van layout with my logo and the Brisco Heat air and plumbing should be in black and red and blue and light blue outlined in white. Have website on sides and phone number. On the botttom of the door i want a section in pink with ribbon and breast cancer awareness. On the other side a dog and cat and says adopt a pet. I have several vans and will want a different awareness on each door.
Industry/Entity Type
It Company
Requirements
Must have
- Red blue white layout like the pic. Big logo. Want the layout and colors of the last pic that has white front.

```html
<!DOCTYPE html>
<html lang="en">
<head>
<meta charset="utf-8">
<title>Brisco Heating &amp; Air Conditioning – Van Wrap</title>
<link rel="stylesheet" href="https://fonts.googleapis.com/css2?family=Michroma&display=swap">
<style>
  :root {
    --wrap-red: #a3141b;
    --wrap-blue: #1d4fc4;
    --wrap-blue-light: #4aa3e8;
    --wrap-white: #f7f8fa;
    --ink: #111216;
    --tire: #1b1b1d;
    --arch: #2c2d31;
    --rim: #c9ccd1;
    --glass: #8e9297;
    --trim: #1f2023;
    --pink: #e0408f;
    --page: #ffffff;
  }
  html, body {
    margin: 0;
    width: 1200px;
    height: 1200px;
    overflow: hidden;
    background: var(--page);
  }
  .wrap-sheet { display: block; width: 1200px; height: 1200px; }
  .brand-text { font-family: "Michroma", sans-serif; }
  .brand-name { fill: var(--ink); font-size: 96px; }
  .brand-tag { font-size: 33px; }
  .tag-heating { fill: var(--wrap-red); }
  .tag-amp { fill: var(--ink); }
  .tag-air { fill: var(--wrap-blue); }
  .phone { fill: var(--wrap-white); font-size: 36px; }
  .website { fill: var(--wrap-white); font-size: 20px; }
  .logo-square { fill: #4a4d52; }
  .tire { fill: var(--tire); }
  .arch { fill: var(--arch); }
  .rim { fill: var(--rim); }
  .hub { fill: #8d9096; }
  .window { fill: var(--glass); }
  .trim { fill: var(--trim); }
  .panel-line { stroke: #c4c7cc; stroke-width: 2; fill: none; }
</style>
</head>
<body>
<svg class="wrap-sheet" viewBox="0 0 1500 1500" xmlns="http://www.w3.org/2000/svg">
  <defs>
    <clipPath id="van-body-clip">
      <path d="M62,455 Q68,402 130,388 L330,348 Q346,342 356,322 L438,222 Q450,210 472,210 L1040,188 Q1370,190 1396,206 Q1411,216 1412,240 L1414,600 L1269,600 A115,115 0 0 0 1051,600 L349,605 A115,115 0 0 0 131,605 L62,605 Z"/>
    </clipPath>
    <linearGradient id="ice-fill" x1="0" y1="0" x2="1" y2="1">
      <stop offset="0" stop-color="#dfe6ee"/>
      <stop offset="1" stop-color="#8f9aa8"/>
    </linearGradient>
    <linearGradient id="pets-fill" x1="0" y1="0" x2="1" y2="0">
      <stop offset="0" stop-color="#e39a45"/>
      <stop offset="1" stop-color="#3a2a24"/>
    </linearGradient>
    <g id="van-shell">
      <circle class="arch" cx="240" cy="640" r="114"/>
      <circle class="arch" cx="1160" cy="640" r="114"/>
      <g clip-path="url(#van-body-clip)">
        <rect x="0" y="150" width="1500" height="500" fill="var(--wrap-white)"/>
        <path d="M0,150 L1100,150 L1070,185 Q900,300 600,405 L330,420 L60,470 L0,470 Z" fill="var(--wrap-red)"/>
        <path d="M1070,185 Q900,300 600,405 L610,412 Q930,305 1110,185 Z" fill="var(--wrap-blue-light)"/>
        <path d="M1070,185 L1110,185 Q1000,250 880,300 Q980,240 1070,185 Z" fill="var(--wrap-blue)"/>
        <path d="M60,480 L330,434 L600,420 L600,428 L330,444 L60,492 Z" fill="var(--wrap-red)"/>
        <path d="M600,625 Q1000,470 1420,400 L1500,400 L1500,700 L600,700 Z" fill="var(--wrap-blue)"/>
        <path d="M640,600 Q1000,470 1420,420 L1420,428 Q1000,485 640,606 Z" fill="var(--wrap-blue-light)"/>
        <path d="M1130,455 Q1300,425 1420,418 L1420,425 Q1300,432 1130,460 Z" fill="var(--wrap-white)"/>
        <path d="M1205,470 L1300,432 L1420,425 L1420,600 L1270,600 L1235,540 Z" fill="url(#ice-fill)" role="img" aria-label="Ice cube artwork"/>
        <path d="M975,590 L1010,522 L1060,512 L1060,600 L975,602 Z" fill="url(#ice-fill)" role="img" aria-label="Ice cube artwork"/>
        <path class="panel-line" d="M336,340 L341,604"/>
        <path class="panel-line" d="M603,208 L608,604"/>
        <rect class="trim" x="62" y="445" width="40" height="95" rx="6"/>
      </g>
      <path class="window" d="M452,228 L564,228 Q576,228 576,240 L576,362 Q576,374 564,374 L392,374 Q381,374 382,362 L384,318 Z"/>
      <path class="trim" d="M362,318 Q356,318 356,328 L356,372 Q356,380 366,380 L382,380 L382,318 Z"/>
      <rect class="trim" x="580" y="432" width="8" height="34" rx="3"/>
      <rect class="trim" x="40" y="545" width="92" height="58" rx="8"/>
      <rect class="trim" x="1398" y="540" width="60" height="54" rx="6"/>
      <rect class="trim" x="349" y="603" width="702" height="12"/>
      <circle class="tire" cx="240" cy="640" r="96"/>
      <circle class="rim" cx="240" cy="640" r="58"/>
      <circle class="hub" cx="240" cy="640" r="22"/>
      <circle class="tire" cx="1160" cy="640" r="96"/>
      <circle class="rim" cx="1160" cy="640" r="58"/>
      <circle class="hub" cx="1160" cy="640" r="22"/>
    </g>
  </defs>

  <!-- Driver side -->
  <g class="van van--driver-side">
    <use href="#van-shell"/>
    <circle cx="466" cy="518" r="72" fill="#f6d2e3" stroke="var(--pink)" stroke-width="6" role="img" aria-label="Pink ribbon badge for October Breast Cancer Awareness Month"/>
    <text class="brand-text website" x="358" y="406" textLength="212" lengthAdjust="spacingAndGlyphs">briscoair.com</text>
    <text class="brand-text phone" transform="translate(638,370) rotate(-24)" textLength="350" lengthAdjust="spacingAndGlyphs">405-555-0187</text>
    <rect class="logo-square" x="640" y="420" width="110" height="110" rx="10" transform="rotate(-15 695 475)"/>
    <text class="brand-text brand-name" transform="translate(780,460) rotate(-15.5)" textLength="575" lengthAdjust="spacingAndGlyphs">BRISCO</text>
    <text class="brand-text brand-tag" transform="translate(792,508) rotate(-16.5)" textLength="580" lengthAdjust="spacingAndGlyphs"><tspan class="tag-heating">Heating</tspan><tspan class="tag-amp"> &amp; </tspan><tspan class="tag-air">Air Conditioning</tspan></text>
  </g>

  <!-- Passenger side -->
  <g class="van van--passenger-side">
    <use href="#van-shell" transform="translate(1500,600) scale(-1,1)"/>
    <rect x="945" y="1068" width="200" height="145" rx="20" fill="url(#pets-fill)" role="img" aria-label="Adopt a Pet artwork with a cat and a dog"/>
    <text class="brand-text website" x="930" y="1006" textLength="212" lengthAdjust="spacingAndGlyphs">briscoair.com</text>
    <text class="brand-text phone" transform="translate(550,842) rotate(22)" textLength="350" lengthAdjust="spacingAndGlyphs">405-555-0187</text>
    <rect class="logo-square" x="165" y="845" width="116" height="116" rx="10" transform="rotate(12 223 903)"/>
    <text class="brand-text brand-name" transform="translate(302,932) rotate(18)" font-size="110" textLength="590" lengthAdjust="spacingAndGlyphs">BRISCO</text>
    <text class="brand-text brand-tag" transform="translate(290,985) rotate(16.6)" textLength="580" lengthAdjust="spacingAndGlyphs"><tspan class="tag-heating">Heating</tspan><tspan class="tag-amp"> &amp; </tspan><tspan class="tag-air">Air Conditioning</tspan></text>
  </g>
</svg>
</body>
</html>
```